Postcard Design

Sir - I am a delivery company in need of a Postcard of 2500ft Van, a 24ft delivery truck and a 40ft delivery truck. My company has to be on the post card and the vehicles as well.
Updates

Reason: Designers must take a look at the home page of my Website@www.trudal.com, and come up with a similar design.

Target Market(s)

Manufacturers, Wholesalers and companies that are in need of Cargo vans and Trucks for bulk deliveries.

Industry/Entity Type

It Company

Colors

Designer to choose colors to be used in the design.

```html
<!DOCTYPE html>
<html lang="en">
<head>
<meta charset="utf-8">
<title>Delivery Company Postcard</title>
<link rel="stylesheet" href="https://fonts.googleapis.com/css2?family=Anton&family=Bowlby+One&family=Open+Sans:wght@400;700&family=Yanone+Kaffeesatz:wght@600&display=swap">
<style>
  :root {
    --page: #e9ebee;
    --navy: #232a6b;
    --ink: #111111;
    --white: #ffffff;
    --yellow: #f5ee1e;
    --stamp: #e3e6e9;
    --sky-deep: #5f8fd0;
    --sky-soft: #b9d2ee;
    --road: #8f8a86;
  }
  * { margin: 0; padding: 0; box-sizing: border-box; }
  html, body { width: 1200px; height: 1138px; overflow: hidden; background: var(--page); }
  .canvas { position: relative; width: 1200px; height: 1138px; }

  .postcard { position: absolute; overflow: hidden; box-shadow: 0 6px 18px rgba(0,0,0,.25); }

  /* Address side */
  .postcard--back { left: 47px; top: 49px; width: 706px; height: 548px; background: var(--white); }
  .back-photo {
    position: absolute; inset: 0;
    background:
      radial-gradient(ellipse 70% 80% at 85% 60%, #ffffff 30%, rgba(255,255,255,0) 75%),
      linear-gradient(180deg, var(--sky-deep) 0%, var(--sky-soft) 45%, #f4f6f8 75%, #ffffff 100%);
  }
  .back-photo__truck {
    position: absolute; left: 0; top: 198px; width: 178px; height: 262px;
    background: linear-gradient(90deg, #d4262a 0%, #d4262a 48%, #c4c9cc 52%, #aeb3b7 100%);
    opacity: .9;
  }
  .back-photo__road {
    position: absolute; left: 0; right: 0; bottom: 0; height: 160px;
    background: linear-gradient(180deg, rgba(150,150,150,.45), rgba(255,255,255,.9));
  }
  .stamp-box { position: absolute; left: 550px; top: 33px; width: 119px; height: 124px; background: var(--stamp); }
  .back-brand {
    position: absolute; left: 40px; top: 36px;
    font-family: 'Anton', sans-serif; font-size: 40px; line-height: 1; color: var(--navy); letter-spacing: -1px;
  }
  .back-phone {
    position: absolute; left: 40px; top: 84px;
    font-family: 'Yanone Kaffeesatz', sans-serif; font-weight: 600; font-size: 44px; line-height: 1; color: var(--ink);
  }
  .back-fleet {
    position: absolute; left: 70px; top: 138px; width: 292px; text-align: center;
    font-family: 'Open Sans', sans-serif; font-size: 19px; line-height: 30px; color: var(--white);
  }

  /* Picture side */
  .postcard--front { left: 440px; top: 540px; width: 715px; height: 556px; }
  .front-photo {
    position: absolute; inset: 0;
    background: linear-gradient(180deg, #5f88cb 0%, #9ab9e2 40%, #c6d6ea 52%, #b7b9bd 58%, #9c9896 72%, var(--road) 100%);
  }
  .front-photo__fleet {
    position: absolute; left: 0; right: 0; top: 290px; height: 135px;
    background: linear-gradient(90deg, #e7d23a 0 14%, #eef0f2 14% 25%, #ee7624 25% 38%, #eef0f2 38% 48%, #a9adb0 48% 62%, #f4f5f6 62% 78%, #c8262b 78% 95%, #d9dbdd 95%);
    opacity: .85;
  }
  .front-brand {
    position: absolute; left: 0; right: 0; top: 48px; text-align: center;
    font-family: 'Anton', sans-serif; font-size: 44px; line-height: 1; color: var(--navy); letter-spacing: -1px;
  }
  .front-fleet {
    position: absolute; left: 0; right: 0; top: 124px; text-align: center;
    font-family: 'Open Sans', sans-serif; font-size: 31px; line-height: 40px; color: var(--white);
  }
  .front-phone {
    position: absolute; left: 0; right: 0; top: 444px; text-align: center;
    font-family: 'Bowlby One', sans-serif; font-size: 40px; line-height: 1; color: var(--yellow); letter-spacing: 3px;
  }
  .front-web {
    position: absolute; left: 0; right: 0; top: 502px; text-align: center;
    font-family: 'Open Sans', sans-serif; font-size: 19px; color: var(--ink);
  }
  b { font-weight: 700; }
</style>
</head>
<body>
<main class="canvas">

  <section class="postcard postcard--back">
    <div class="back-photo" role="img" aria-label="Photo of a red articulated truck on a highway under a bright blue sky, fading to white">
      <div class="back-photo__truck"></div>
      <div class="back-photo__road"></div>
    </div>
    <div class="stamp-box"></div>
    <h1 class="back-brand">DELIVERY COMPANY</h1>
    <p class="back-phone">CALL US 123 456 789</p>
    <ul class="back-fleet" style="list-style:none">
      <li>2500FT <b>VAN</b></li>
      <li>24FT <b>DELIVERY TRUCK</b></li>
      <li>40FT <b>DELIVERY TRUCK</b></li>
    </ul>
  </section>

  <section class="postcard postcard--front">
    <div class="front-photo" role="img" aria-label="Photo of a row of parked semi trucks in yellow, orange, silver, white and red under a blue sky">
      <div class="front-photo__fleet"></div>
    </div>
    <h2 class="front-brand">DELIVERY COMPANY</h2>
    <ul class="front-fleet" style="list-style:none">
      <li>2500FT <b>VAN</b></li>
      <li>24FT <b>DELIVERY TRUCK</b></li>
      <li>40FT <b>DELIVERY TRUCK</b></li>
    </ul>
    <p class="front-phone">CALL US 123 456 789</p>
    <p class="front-web">WWW.HAULWAY.COM</p>
  </section>

</main>
</body>
</html>
```